New Business Card Design Project

We need to enhance the look and feel of our brand. We are starting with the business card and will hopefully expand to letter head, website, etc. The firm is based in Kolding Denmark and invests with global pension funds and for mutual fund investors alike. We would like to see an innovative use of the companies logo (star on the website - www.northmerrowcap.com) and a broader use of a color palette. Presently it is dominantly shades of blue. The firm wants to convey a sense they are a creative investment team that understands all the risks in the emerging markets and have the skills to perform in an environment of uncertainty.

Presently, we have three locations: Kolding Denmark, Glendale CA USA, Zurich Switzerland. We also have a prominently displayed bar code square on a solid dark blue back that will take smart phone users to the firm's website. I am indifferent to its inclusion., Details for my new Business Card Design Project will be added soon.
Updates

Project Deadline Extended
Reason: Designers, I am working with on getting feedback from both US and Danish partners on preferences. That is taking slightly more time than expected. Thanks for you patience. Nice work. TLV

Target Market(s)

The target market is a combination of institutional and retail investors. The european arm uses a card similar to a couple of those submitted.

Industry/Entity Type

Environment

Requirements
Must have
• The company's Star Logo. See www.northmerrowcap.com. It may be used in its current form or some new clever way. The founders are Danish and have a strong affinity for it.
Nice to have
• The new materials may be solely used in the north America and distributed in Australia as well. Therefore, we may try something new in these markets. I'd prefer to see a broader use of the color spectrum, not simply blue.
Should not have
• The card should not look and feel like a bank, insurance company, or a traditional money manager.

```html
<!DOCTYPE html>
<html lang="en">
<head>
<meta charset="utf-8">
<title>Northmerrow Capital – Business Card</title>
<link rel="stylesheet" href="https://fonts.googleapis.com/css2?family=Source+Sans+3:wght@400;600&family=Crimson+Text:wght@600&display=swap">
<style>
  :root {
    --orange: #f7941d;
    --navy: #1f3f7d;
    --navy-deep: #18336a;
    --ring: #5fb0dc;
    --white: #ffffff;
    --ink: #1f3f7d;
    --peach: #fbdcc0;
    --backdrop: #e4e4e4;
  }
  * { box-sizing: border-box; margin: 0; padding: 0; }
  html, body {
    width: 1200px;
    height: 638px;
    overflow: hidden;
    background: var(--backdrop);
    font-family: "Source Sans 3", Arial, sans-serif;
  }
  .stage {
    position: relative;
    width: 1200px;
    height: 638px;
  }
  .card {
    position: absolute;
    top: 164px;
    width: 540px;
    height: 310px;
    overflow: hidden;
    box-shadow: 0 6px 18px rgba(0,0,0,0.18);
  }

  /* Brand side */
  .card--front {
    left: 630px;
    background: var(--orange);
  }
  .front-mark {
    position: absolute;
    left: 60px;
    top: 75px;
    width: 160px;
    height: 160px;
  }
  .front-text {
    position: absolute;
    left: 240px;
    top: 96px;
    width: 280px;
  }
  .front-name {
    color: var(--white);
    font-weight: 400;
    font-size: 40px;
    line-height: 40px;
    letter-spacing: 0.3px;
    white-space: nowrap;
  }
  .front-url {
    margin-top: 10px;
    color: var(--navy);
    font-size: 18px;
    font-weight: 400;
    white-space: nowrap;
  }

  /* Contact side */
  .card--back {
    left: 30px;
    background: var(--white);
  }
  .back-band {
    position: absolute;
    left: 0;
    top: 0;
    width: 100%;
    height: 126px;
    background: var(--navy);
  }
  .back-brand {
    position: absolute;
    left: 26px;
    top: 22px;
    display: flex;
    align-items: center;
    gap: 12px;
  }
  .back-brand svg { width: 42px; height: 42px; }
  .back-brand-name {
    color: var(--white);
    font-size: 30px;
    font-weight: 400;
    letter-spacing: 0.3px;
    white-space: nowrap;
  }
  .back-locations {
    position: absolute;
    left: 26px;
    top: 92px;
    color: var(--orange);
    font-family: "Crimson Text", Georgia, serif;
    font-weight: 600;
    font-size: 17px;
    white-space: nowrap;
  }
  .back-decor {
    position: absolute;
    right: -60px;
    bottom: -90px;
    width: 300px;
    height: 300px;
  }
  .contact {
    position: absolute;
    left: 26px;
    top: 140px;
    color: var(--ink);
    font-size: 18px;
    line-height: 22px;
  }
  .contact-name {
    font-weight: 600;
    font-size: 21px;
    line-height: 26px;
  }
</style>
</head>
<body>
<main class="stage">

  <section class="card card--back" aria-label="Business card, contact side">
    <svg class="back-decor" viewBox="0 0 300 300" aria-hidden="true">
      <circle cx="150" cy="150" r="150" fill="var(--peach)"/>
    </svg>
    <div class="back-band">
      <div class="back-brand">
        <svg viewBox="0 0 42 42" aria-hidden="true">
          <circle cx="21" cy="21" r="19" fill="var(--ring)"/>
        </svg>
        <span class="back-brand-name">Northmerrow Capital</span>
      </div>
      <p class="back-locations">Kolding, Denmark | Glendale, CA, USA | Zurich, Switzerland</p>
    </div>
    <div class="contact">
      <p class="contact-name">Aren Holt</p>
      <p>chief operating officer</p>
      <p>aren.holt@northmerrowcap.com</p>
      <p>404.555.0182</p>
      <p>404.555.0147</p>
    </div>
  </section>

  <section class="card card--front" aria-label="Business card, brand side">
    <svg class="front-mark" viewBox="0 0 160 160" aria-hidden="true">
      <circle cx="80" cy="80" r="80" fill="var(--navy-deep)"/>
    </svg>
    <div class="front-text">
      <p class="front-name">Northmerrow<br>Capital</p>
      <p class="front-url">www.northmerrowcap.com</p>
    </div>
  </section>

</main>
</body>
</html>
```